Marlow crest Letter head

Need a heeder and footer for 8.5 x 11 paper
2 inch top header, 1.5 inch bottom footer
Add logo, agent pictures, names and titles (Broker), office picture with address
Marlow Crest Real Estate
20387 Route 512
Wrenfield Cove, SC 29000
Please make phone # large (555) 304-7182
MarlowCrestRealEstate.example

```html
<!DOCTYPE html>
<html lang="en">
<head>
<meta charset="utf-8">
<title>Marlow Crest Letterhead</title>
<link href="https://fonts.googleapis.com/css2?family=Encode+Sans+Condensed:wght@400&family=Lato:wght@400;700;900&display=swap" rel="stylesheet">
<style>
  :root {
    --backdrop: #d6d6d6;
    --paper: #ffffff;
    --brand-red: #d0202a;
    --brand-navy: #1f2460;
    --text: #4a4a4a;
    --photo-blue: #2f6fb8;
    --photo-blue-deep: #1c4f93;
  }
  * { box-sizing: border-box; margin: 0; padding: 0; }
  html, body { width: 1056px; height: 1200px; overflow: hidden; }
  body {
    background: var(--backdrop);
    font-family: "Lato", sans-serif;
    color: var(--text);
    position: relative;
  }
  .letterhead {
    position: absolute;
    left: 104px; top: 0;
    width: 848px; height: 1200px;
    background: var(--paper);
  }
  .brand-name {
    position: absolute;
    left: 85px; top: 98px;
    width: 182px;
    font-weight: 900;
    font-size: 29px;
    line-height: 1;
    color: var(--brand-navy);
    text-align: center;
    letter-spacing: 0.5px;
  }
  .portrait {
    position: absolute;
    top: 64px;
    width: 112px; height: 112px;
    border-radius: 50%;
    border: 2px solid var(--brand-red);
    padding: 4px;
  }
  .portrait span {
    display: block; width: 100%; height: 100%; border-radius: 50%;
    background: radial-gradient(circle at 50% 40%, var(--photo-blue), var(--photo-blue-deep));
  }
  .portrait.agent-one { left: 387px; }
  .portrait.agent-two { left: 524px; }
  .portrait.office { left: 658px; }
  .portrait.office span { background: linear-gradient(180deg, #c7d3dd 0%, #6d86a8 45%, #8a8c8e 100%); }
  .header-rule {
    position: absolute; left: 82px; top: 192px;
    width: 688px; height: 2px; background: var(--brand-red);
  }
  .letter-body {
    position: absolute; left: 82px; top: 356px; width: 688px;
    font-family: "Encode Sans Condensed", sans-serif;
    font-size: 18.5px; line-height: 29.5px;
  }
  .letter-body p { text-align: justify; margin-bottom: 29px; }
  .salutation { margin-bottom: 25px !important; }
  .closing {
    position: absolute; left: 82px; top: 946px;
    font-family: "Encode Sans Condensed", sans-serif;
    font-size: 18.5px;
  }
  .signature {
    position: absolute; left: 80px; top: 990px;
    width: 70px; height: 46px;
    background: #f7e1e2;
  }
  .footer-address {
    position: absolute; right: 460px; top: 1100px;
    text-align: right; font-size: 16.5px; line-height: 19.5px;
    font-style: normal;
  }
  .footer-divider {
    position: absolute; left: 424px; top: 1099px;
    width: 2px; height: 60px; background: var(--brand-red);
  }
  .footer-contacts {
    position: absolute; left: 452px; top: 1093px;
    list-style: none; font-size: 16.5px; line-height: 22px;
  }
  .footer-contacts li { display: flex; align-items: center; gap: 14px; }
  .footer-contacts svg { width: 15px; height: 15px; flex: none; }
</style>
</head>
<body>
  <main class="letterhead">
    <header>
      <div class="brand-name">Marlow Crest</div>
      <div class="portrait agent-one" role="img" aria-label="Broker portrait photo"><span></span></div>
      <div class="portrait agent-two" role="img" aria-label="Broker portrait photo"><span></span></div>
      <div class="portrait office" role="img" aria-label="Office building photo"><span></span></div>
      <div class="header-rule"></div>
    </header>

    <section class="letter-body">
      <p class="salutation">Dear Sir/Mam,</p>
      <p>Contrary to popular belief, Lorem Ipsum is not simply random text. It has roots in a piece of classical Latin literature from 45 BC, making it over 2000 years old. Harold Pennick, a Latin professor at Ashford Hill College in Virginia, looked up one of the more obscure Latin words, consectetur.</p>
      <p>Lorem Ipsum comes from sections 1.10.32 and 1.10.33 of "de Finibus Bonorum et Malorum" (The Extremes of Good and Evil) by Varelius, written in 45 BC. This book is a treatise on the theory of ethics, very popular during the Renaissance. The first line of Lorem Ipsum.</p>
      <p>The standard chunk of Lorem Ipsum used since the 1500s is reproduced below for those interested. Sections 1.10.32 and 1.10.33 from "de Finibus Bonorum et Malorum" by Varelius are also reproduced in their exact original.</p>
      <p>The standard chunk of Lorem Ipsum used since the 1500s is reproduced below for those interested.</p>
    </section>

    <p class="closing">Best Regards</p>
    <div class="signature" role="img" aria-label="Handwritten signature"></div>

    <footer>
      <address class="footer-address">
        Marlow Crest Real Estate<br>
        20387 Route 512<br>
        Wrenfield Cove, SC 29000
      </address>
      <div class="footer-divider"></div>
      <ul class="footer-contacts">
        <li>
          <svg viewBox="0 0 16 16"><path d="M3 1.5l3 .5 1 3.5-2 1.2a9 9 0 0 0 4.3 4.3l1.2-2 3.5 1 .5 3c-.2.8-1 1.5-2 1.5C6.8 14.5 1.5 9.2 1.5 3.5c0-1 .7-1.8 1.5-2z" fill="#d0202a"/></svg>
          (555) 304-7182
        </li>
        <li>
          <svg viewBox="0 0 16 16"><rect x="1" y="3" width="14" height="10" fill="#d0202a"/><path d="M1.5 3.5L8 9l6.5-5.5" stroke="#fff" stroke-width="1.3" fill="none"/></svg>
          info@MarlowCrestRealEstate.example
        </li>
        <li>
          <svg viewBox="0 0 16 16" fill="none" stroke="#d0202a" stroke-width="1.2"><circle cx="8" cy="8" r="6.5"/><ellipse cx="8" cy="8" rx="3" ry="6.5"/><path d="M1.5 8h13M2.5 5h11M2.5 11h11"/></svg>
          www.MarlowCrestRealEstate.example
        </li>
      </ul>
    </footer>
  </main>
</body>
</html>
```